HARLOWE CONSERVATORY SAXOPHONE SENIOR RECITAL

I need a poster design for my senior saxophone recital. The title of it is "Quill: a Voyage beneath the Edge of Tone". My concept is completely contrasting to the idea of a typical university recital. I'm so put off by the idea of "clap..clap..{play some music}..clap..clap..repeat". My recital is all based off of sound. The music I selected is all very modern (i.e Brem Ostrakel 'Warm from the First Pour' for Saxophone and Coffee Machine). I've included the Chatterbox link so you can see the picture I have in the background. I like the idea of minimal black and white photography. Also, I would like the time / date / location / etc. all included on it. Let your imaginations run wild! It's art for an artist!
https://www.chatterbox-example.net/events/412093857716230/
Target Market(s)
University Students around the Harlowe Conservatory and locals around the art district of South Beach, FL.
Industry/Entity Type
University
Look and feel

```html
<!DOCTYPE html>
<html lang="en">
<head>
<meta charset="utf-8">
<title>Quill: a Voyage beneath the Edge of Tone</title>
<link rel="stylesheet" href="https://fonts.googleapis.com/css2?family=Open+Sans:wght@800&family=Source+Sans+3:wght@400&display=swap">
<style>
  :root {
    --sheet: #ffffff;
    --ink-black: #050505;
    --haze-light: #d9d3c8;
    --haze-blue: #b9c2c8;
    --haze-mid: #8c8377;
    --haze-dark: #2e2b28;
    --title-fill: rgba(120, 112, 104, 0.72);
    --title-edge: rgba(30, 28, 26, 0.6);
    --subtitle: #857668;
    --detail: #b3a393;
  }
  * { margin: 0; padding: 0; box-sizing: border-box; }
  html, body {
    width: 794px;
    height: 1200px;
    overflow: hidden;
    background: var(--sheet);
  }
  .poster {
    position: absolute;
    left: 9px;
    top: 8px;
    width: 776px;
    height: 1187px;
    background: var(--ink-black);
    overflow: hidden;
  }
  .backdrop-photo {
    position: absolute;
    inset: 0;
    background:
      radial-gradient(ellipse 38% 22% at 62% 14%, var(--haze-blue) 0%, rgba(185,194,200,0) 100%),
      radial-gradient(ellipse 60% 40% at 45% 28%, var(--haze-light) 0%, rgba(217,211,200,0) 100%),
      radial-gradient(ellipse 30% 22% at 88% 45%, var(--haze-dark) 0%, rgba(46,43,40,0) 100%),
      linear-gradient(180deg, var(--haze-mid) 0%, #6f675e 35%, #3b3733 58%, #141312 75%, var(--ink-black) 92%);
  }
  .title-block {
    position: absolute;
    left: 43px;
    top: 722px;
  }
  .title {
    font-family: "Open Sans", sans-serif;
    font-weight: 800;
    font-size: 162px;
    line-height: 1;
    letter-spacing: 2px;
    color: var(--title-fill);
    -webkit-text-stroke: 1px var(--title-edge);
  }
  .subtitle {
    margin-top: 0;
    padding-left: 3px;
    font-family: "Source Sans 3", sans-serif;
    font-size: 31px;
    color: var(--subtitle);
  }
  .details {
    position: absolute;
    left: 45px;
    font-family: "Source Sans 3", sans-serif;
    color: var(--detail);
  }
  .when {
    top: 980px;
    font-size: 30px;
    line-height: 43px;
  }
  .where {
    top: 1096px;
    font-size: 24px;
    line-height: 34px;
  }
</style>
</head>
<body>
  <main class="poster">
    <div class="backdrop-photo" role="img" aria-label="Blurred black and white photograph of a saxophonist in motion, light streaks fading into darkness"></div>
    <header class="title-block">
      <h1 class="title">QUILL</h1>
      <p class="subtitle">A Voyage Beneath the Edge of Tone</p>
    </header>
    <p class="details when">December 8<br>2pm</p>
    <p class="details where">Elias T. Marrow Recital Hall<br>Coral Gables, Florida</p>
  </main>
</body>
</html>
```